Meadow Lantern Veterinary Practice including Nest2Grow

We require a double-sided full colour tri-fold Brochure for Print.
Colour theme to in line with logo below

Written CONTENT below
Orphans
We can provide care and a new mother for orphan foals of any age, breed or size, from thoroughbreds and draft breeds to tiny ponies and even donkeys.
We have successfully fostered orphans from a few hours of age through to eight weeks, regardless of how long or if at all they were with their birth mother, and of previous fostering attempts.
We have the knowledge and experience to provide optimum nutrition and care to orphans during the brief period that they don’t have a mum, until their new foster mother is ready to take them.
Additionally we are a veterinary practice, and can provide diagnostics and therapeutics for compromised orphan foals such as plasma administration and health checks.

Mares
Nest2Grow mares have been selected for mothering ability and temperament, and have all carried and raised at least one foal of their own. Many have already been successful foster mothers in one or more of the last five breeding seasons.
The mares are not currently pregnant and are given a carefully designed course of hormones to induce lactation when required. The milk produced is not colostrum, but is completely normal and equivalent to that which they would have had if the foal was theirs by birth.
There is published scientific information (in addition to our own experience and that of the owners of previous graduates of our programme) that growth and development of foals raised by induced lactation is identical to that of foals raised by their birth mothers.

Fostering
During the few days when the mare’s udder is developing, mare and foal are kept next separately but in close proximity, allowing bonding to begin and reducing stress on the orphan.
The fostering is completed once the mare has enough milk to feed the foal, and our experienced handlers ensure that joining the two goes smoothly.
Once they are together the mare completely accepts the foal as her own, and the foal can suckle freely – at this stage we continue to offer supplementary feeds until they are not needed.
The mare and foal are then a normal unit and can return to the foal owner’s care until weaning – ensuring optimum nutrition and behaviour for the foal and excellent outcomes in performance, relationships with other horses, and interaction with humans.

Complete Safety
Mares recognise their birth foal by scent - a unique bond established during the first few minutes of the foal’s life - and only a small percentage of mares who have lost their own foal will readily accept a substitute.
When a mare who has lost her birth foal is offered an orphan, it is very normal and common for her to respond with aggression - to the danger of the foal and the human handler.
Nest2Grow mares have no birth foal in the current season, and are happy to adopt any foal who is placed close to them during the hormone treatment period.
This makes for total foal and handler safety.

Excellent Success Rate
After seven years of perfecting the fostering method, Nest2Grow can claim total success: we have now documented almost 50 fosterings over the last five breeding seasons. We have never been entrusted with an orphan foal that we have not been able to provide with a beautiful foster mum.

Career Mothers
Being dedicated career mothers with no other job in life, our mares are free to accompany their new foals home and stay with them as long as required. No foals are weaned and left without a mother in our programme, and our beautiful mares who would otherwise not be bred, are given a foal every year and a wonderful lifelong purpose.

Every single orphan’s human family has admired and appreciated our beautiful mares, with many offering to give them a home for life. Each season as the orphans are weaned, we welcome our mares home to Meadow Lantern to prepare for the next foal in need – a job they totally love! – just as if they were in a natural breeding situation.

Meadow Lantern Vet Practice including Nest2Grow
214 Pellerby Lane
Thornvale. Vic. 3812

Phone 0431958617 or 0419284056

```html
<!DOCTYPE html>
<html lang="en">
<head>
<meta charset="utf-8">
<title>Nest2Grow – Orphan Foal Fostering Brochure Spread</title>
<link href="https://fonts.googleapis.com/css2?family=Archivo:wght@400;700&display=swap" rel="stylesheet">
<style>
  :root {
    --canvas: #ffffff;
    --panel-light: #f8a63c;
    --panel-mid: #f48f36;
    --panel-deep: #f07a30;
    --band-start: #ec4a3c;
    --band-end: #f3813a;
    --ink: #111111;
    --band-text: #ffffff;
    --rule: #4a3a30;
    --photo-stable-a: #6b5a48;
    --photo-stable-b: #b79a70;
    --photo-field-a: #3e3a30;
    --photo-field-b: #6a5040;
  }
  * { box-sizing: border-box; margin: 0; padding: 0; }
  html, body { width: 1200px; height: 1000px; overflow: hidden; background: var(--canvas); }
  body { position: relative; font-family: "Archivo", Arial, sans-serif; color: var(--ink); }

  .spread { position: absolute; left: 113px; top: 202px; width: 843px; height: 596px;
    background: linear-gradient(180deg, var(--panel-light) 0%, var(--panel-mid) 55%, var(--panel-deep) 100%);
    border: 1px solid var(--rule); }

  .photo { position: absolute; }
  .photo--stable { left: 0; top: 0; width: 282px; height: 387px;
    background: linear-gradient(160deg, var(--photo-stable-a) 0%, #8a7358 45%, var(--photo-stable-b) 100%); }
  .photo--paddock { left: 282px; top: 395px; width: 560px; height: 200px;
    background: linear-gradient(100deg, var(--photo-field-a) 0%, var(--photo-field-b) 50%, #4a4a40 100%); }

  .divider { position: absolute; width: 1px; background: var(--rule); }
  .divider--a { left: 281px; top: 0; height: 596px; }
  .divider--b { left: 561px; top: 0; height: 395px; }

  .band { position: absolute; height: 19px; padding-left: 15px;
    background: linear-gradient(90deg, var(--band-start), var(--band-end));
    color: var(--band-text); font-weight: 700; font-size: 12.5px; line-height: 19px; }

  .copy { position: absolute; font-size: 8.6px; line-height: 10.6px; }
  .copy p + p { margin-top: 10.6px; }

  .band--orphans { left: 0; top: 387px; width: 282px; }
  .copy--orphans { left: 16px; top: 412px; width: 250px; }

  .copy--vet { left: 297px; top: 22px; width: 250px; }
  .band--mares { left: 282px; top: 73px; width: 279px; }
  .copy--mares { left: 297px; top: 104px; width: 252px; }
  .band--fostering { left: 282px; top: 288px; width: 279px; }
  .copy--fostering { left: 297px; top: 313px; width: 250px; }

  .copy--joining { left: 574px; top: 22px; width: 256px; }
  .band--safety { left: 562px; top: 187px; width: 280px; }
  .copy--safety { left: 574px; top: 213px; width: 256px; }
</style>
</head>
<body>
  <section class="spread">
    <div class="photo photo--stable" role="img" aria-label="Woman bottle-feeding a bay foal inside a stable stall with straw bedding"></div>

    <div class="divider divider--a"></div>
    <div class="divider divider--b"></div>

    <h2 class="band band--orphans">Orphans</h2>
    <div class="copy copy--orphans">
      <p>We can provide care and a new mother for orphan foals of any age, breed or size, from thoroughbreds and draft breeds to tiny ponies and even donkeys.</p>
      <p>We have successfully fostered orphans from a few hours of age through to eight weeks, regardless of how long or if at all they were with their birth mother, and of previous fostering attempts.</p>
      <p>We have the knowledge and experience to provide optimum nutrition and care to orphans during the brief period that they don’t have a mum, until their new foster mother is ready to take them.</p>
    </div>

    <div class="copy copy--vet">
      <p>Additionally we are a veterinary practice, and can provide diagnostics and therapeutics for compromised orphan foals such as plasma administration and health checks.</p>
    </div>

    <h2 class="band band--mares">Maresi</h2>
    <div class="copy copy--mares">
      <p>Nest2Grow mares have been selected for mothering ability and temperament, and have all carried and raised at least one foal of their own. Many have already been successful foster mothers in one or more of the last five breeding seasons.</p>
      <p>The mares are not currently pregnant and are given a carefully designed course of hormones to induce lactation when required. The milk produced is not colostrum, but is completely normal and equivalent to that which they would have had if the foal was theirs by birth.</p>
      <p>There is published scientific information (in addition to our own experience and that of the owners of previous graduates of our programme) that growth and development of foals raised by induced lactation is identical to that of foals raised by their birth mothers.</p>
    </div>

    <h2 class="band band--fostering">Fostering</h2>
    <div class="copy copy--fostering">
      <p>During the few days when the mare’s udder is developing, mare and foal are kept next separately but in close proximity, allowing bonding to begin and reducing stress on the orphan..</p>
    </div>

    <div class="copy copy--joining">
      <p>The fostering is completed once the mare has enough milk to feed the foal, and our experienced handlers ensure that joining the two goes smoothly.</p>
      <p>Once they are together the mare completely accepts the foal as her own, and the foal can suckle freely – at this stage we continue to offer supplementary feeds until they are not needed.</p>
      <p>The mare and foal are then a normal unit and can return to the foal owner’s care until weaning – ensuring optimum nutrition and behaviour for the foal and excellent outcomes in performance, relationships with other horses, and interaction with humans.</p>
    </div>

    <h2 class="band band--safety">Complete Safety</h2>
    <div class="copy copy--safety">
      <p>Mares recognise their birth foal by scent - a unique bond established during the first few minutes of the foal’s life - and only a small percentage of mares who have lost their own foal will readily accept a substitute.</p>
      <p>When a mare who has lost her birth foal is offered an orphan, it is very normal and common for her to respond with aggression - to the danger of the foal and the human handler.</p>
      <p>Nest2Grow mares have no birth foal in the current season, and are happy to adopt any foal who is placed close to them during the hormone treatment period.</p>
      <p>This makes for total foal and handler safety.</p>
    </div>

    <div class="photo photo--paddock" role="img" aria-label="Bay mare with a young dark foal and a handler standing in a tree-lined paddock"></div>
  </section>
</body>
</html>
```